Brightway Talent Partners, LLC Business Card Design

Website URL: www.brightwaytalentpartners-example.com
I have attached a previous design that I find "okay" and adequate, but I wanted to explore some more distinctive/creative professional versions.
Our company provides business owners, executives and managers valuable information to help them make better people decisions. Our primary means of providing this information is through a comprehensive suite of employee assessment products across the employee life cycle that help clients better select, manage and retain talent. Company tagline is: Assess People, Predict Performance. Our employee assessment products fall into the following 3 categories:
- Assessments for Hiring Talent
- Assessments for Developing Talent
- Assessments for Retaining Talent
Please view our 3 minute overview video (link below) to get a sense of who we are:
http://videohost-example.com/q9Rt2LmXw8b
Our business personality is competent, modern, & friendly...driven by developing long lasting client relationships as opposed to one time customer transactions. We would like to see designs that are professional yet distinctive "cool business card!" and use primary logo colors/complementary color . Not sure if I prefer the gray font as shown in previous design or black...open to suggestions.
The final design should communicate competence, trust, and solutions. Also, I am an authorized business partner and consultant with two organizations that provide the assessment products I will market/use with clients. Attached are files for Meridale Worldwide and Tollard Worldwide that should be incorporated into the design (*very small but readable)

Industry/Entity Type
Business
Contact Information for Business Card
Dwight Halvers
Founder and Managing Partner
4381 North Juniper Mill Lane
Suite 715
Atlanta GA 30419-5183
Office: 555.014.2796
dhalvers@brightwaytalentpartners-example.com
www.brightwaytalentpartnrs-example.com

```html
<!DOCTYPE html>
<html lang="en">
<head>
<meta charset="utf-8">
<title>Brightway Talent Partners – Business Card</title>
<link rel="stylesheet" href="https://fonts.googleapis.com/css2?family=Questrial&display=swap">
<style>
  :root {
    --cyan: #22b7e8;
    --mid-blue: #1a86cf;
    --deep-blue: #1d3d8c;
    --navy: #17337a;
    --white: #ffffff;
    --ink: #1f2a44;
    --muted: #6b7488;
    --band-light: #35c3ee;
    --soft-white: rgba(255,255,255,0.82);
  }
  * { margin: 0; padding: 0; box-sizing: border-box; }
  html, body { width: 1200px; height: 703px; overflow: hidden; background: #e9edf2; }
  .card {
    position: relative;
    width: 1200px; height: 703px;
    overflow: hidden;
    font-family: "Questrial", "Century Gothic", sans-serif;
    color: var(--white);
    background: linear-gradient(90deg, var(--cyan) 0%, var(--mid-blue) 35%, #1f5fb2 65%, var(--deep-blue) 100%);
  }
  .globe-area {
    position: absolute;
    left: 620px; top: -40px;
    width: 640px; height: 700px;
    border-radius: 50%;
    background: radial-gradient(circle at 55% 45%, rgba(120,190,240,0.35) 0%, rgba(60,120,200,0.25) 45%, rgba(29,61,140,0) 72%);
  }

  .brand {
    position: absolute;
    left: 66px; top: 38px;
  }
  .brand-name { font-size: 34px; line-height: 1.1; letter-spacing: 0.3px; }
  .brand-tagline {
    margin-top: 8px;
    font-size: 17px; letter-spacing: 2px; text-transform: uppercase;
    color: var(--soft-white);
    padding-left: 14px;
    border-left: 3px solid var(--band-light);
  }

  .person {
    position: absolute;
    right: 66px; top: 470px;
    text-align: right;
  }
  .person-name { font-size: 44px; line-height: 1.1; }
  .person-title {
    margin-top: 10px;
    font-size: 20px; letter-spacing: 1px;
    color: var(--soft-white);
  }
  .person-rule {
    display: block;
    width: 120px; height: 3px;
    margin: 14px 0 0 auto;
    background: var(--band-light);
  }

  .partner-box {
    position: absolute;
    left: 66px; top: 150px;
    width: 366px; height: 174px;
    background: var(--white);
    border-radius: 0 6px 6px 0;
    color: var(--ink);
    padding: 14px 0 0 20px;
  }
  .partner-label { font-size: 13px; letter-spacing: 0.2px; }
  .partner {
    display: flex; align-items: center; gap: 10px;
    margin-top: 14px;
  }
  .partner-mark {
    width: 34px; height: 34px; border-radius: 50%;
    background: var(--mid-blue);
  }
  .partner-name { font-size: 26px; color: var(--navy); line-height: 1; }
  .partner-sub { font-size: 12px; color: var(--muted); margin: 3px 0 0 64px; }
  .partner-second { margin-top: 10px; }
  .partner-second .partner-name { font-size: 22px; color: #3d4a66; }
  .partner-second + .partner-sub { margin-left: 64px; }

  .contact-list { position: absolute; left: 0; top: 424px; list-style: none; }
  .contact-row {
    display: flex; align-items: flex-start;
    height: 40px;
    font-size: 25px; line-height: 36px;
  }
  .contact-row.address { height: 82px; }
  .icon-tab {
    width: 93px; height: 32px;
    margin-top: 2px;
    background: var(--white);
    border-radius: 0 16px 16px 0;
    display: flex; align-items: center; justify-content: flex-end;
    padding-right: 14px;
    flex-shrink: 0;
  }
  .icon-tab svg { width: 24px; height: 24px; }
  .contact-text { margin-left: 16px; white-space: nowrap; }

  .bottom-band {
    position: absolute; left: 0; bottom: 0;
    width: 100%; height: 40px;
    background: linear-gradient(90deg, #1e9ad8 0%, #2e72c2 60%, #2e5fb4 100%);
    border-top: 4px solid var(--band-light);
  }
</style>
</head>
<body>
<div class="card">
  <div class="globe-area" role="img" aria-label="Stylised globe showing world continents"></div>

  <header class="brand">
    <h1 class="brand-name">Brightway Talent Partners, LLC</h1>
    <p class="brand-tagline">Assess People, Predict Performance</p>
  </header>

  <div class="partner-box">
    <p class="partner-label">Authorized Business Partner and Consultant</p>
    <div class="partner">
      <span class="partner-mark"></span>
      <span class="partner-name">Tollard Worldwide</span>
    </div>
    <p class="partner-sub">Certified Consultant</p>
    <div class="partner partner-second">
      <span class="partner-name">Meridale Worldwide</span>
    </div>
    <p class="partner-sub">a global assessment company</p>
  </div>

  <div class="person">
    <h2 class="person-name">Dwight Halvers</h2>
    <p class="person-title">Founder and Managing Partner</p>
    <span class="person-rule"></span>
  </div>

  <ul class="contact-list">
    <li class="contact-row address">
      <span class="icon-tab">
        <svg viewBox="0 0 24 24" fill="none" stroke="#1d3d8c" stroke-width="2.2"><path d="M12 22s7-7.5 7-13a7 7 0 0 0-14 0c0 5.5 7 13 7 13z"/><circle cx="12" cy="9" r="2.6"/></svg>
      </span>
      <span class="contact-text">4381 North Juniper Mill Lane<br>Suite 715 Atlanta GA 30419-5183</span>
    </li>
    <li class="contact-row">
      <span class="icon-tab">
        <svg viewBox="0 0 24 24" fill="none" stroke="#1d3d8c" stroke-width="2"><circle cx="12" cy="12" r="10"/><path d="M8.5 7.5l2 2-1.2 1.6a7 7 0 0 0 3.6 3.6l1.6-1.2 2 2-1.4 1.6c-3.6-.4-7.8-4.6-8.2-8.2z"/></svg>
      </span>
      <span class="contact-text">555.014.2796</span>
    </li>
    <li class="contact-row">
      <span class="icon-tab">
        <svg viewBox="0 0 24 24" fill="none" stroke="#1d3d8c" stroke-width="2"><rect x="3" y="6" width="18" height="13" rx="1"/><path d="M3 7l9 7 9-7"/></svg>
      </span>
      <span class="contact-text">dhalvers@brightwaytalentpartners-example.com</span>
    </li>
    <li class="contact-row">
      <span class="icon-tab">
        <svg viewBox="0 0 24 24" fill="none" stroke="#1d3d8c" stroke-width="2"><circle cx="12" cy="12" r="10"/><ellipse cx="12" cy="12" rx="4.5" ry="10"/><path d="M2 12h20M4 7h16M4 17h16"/></svg>
      </span>
      <span class="contact-text">www.brightwaytalentpartnrs-example.com</span>
    </li>
  </ul>

  <div class="bottom-band"></div>
</div>
</body>
</html>
```